Label Design for a New Alcoholized Root Beer

Create a design for a new alcoholized root beer. This is a new product category in the USA growing very rapidly. Root Beer is a popular flavor of Cola, but recently, beer manufacturers have added alcohol to it and have created a new product that has gained traction on the market at a tremendous rate.

Root Beer is vintage product that has been around for a hundred years. Consumers of this product are mostly male between the age of 30 to 45. They purchase this product for its nostalgia and vintage look and taste.

This product will be in a standard 355 mL brown bottle.

It is 5.9% abv.

The name of the product is ''Corvel's Hard Root Beer''.

We have uploaded some pictures of traditional root beers to give you an idea of the feel we want our product to have and also, the bottle the product will be filled in.

Target Market(s)

Consumers are male 30-45, same market as craft beer consumers

Industry/Entity Type

Product

Requirements
Must have
• Design must have a vintage feel to it

```html
<!DOCTYPE html>
<html lang="en">
<head>
<meta charset="utf-8">
<title>Corvel's Hard Root Beer — Label</title>
<link rel="stylesheet" href="https://fonts.googleapis.com/css2?family=Alfa+Slab+One&family=Oswald:wght@500&display=swap">
<style>
  :root {
    --label-brown: #3b2418;
    --label-brown-deep: #2a170f;
    --cream: #f2e4c9;
    --tan: #a8865f;
    --tan-dark: #7c5f40;
    --blue: #3f73ad;
    --blue-soft: #5b8cc4;
  }
  html, body {
    margin: 0;
    padding: 0;
    width: 800px;
    height: 1200px;
    overflow: hidden;
    background: var(--label-brown-deep);
  }
  .label {
    position: relative;
    width: 800px;
    height: 1200px;
    background: radial-gradient(ellipse at 50% 40%, #4a2e1f 0%, var(--label-brown) 55%, var(--label-brown-deep) 100%);
    color: var(--cream);
    text-align: center;
  }
  .star-row {
    position: absolute;
    top: 110px;
    left: 0;
    width: 100%;
  }
  .brand-name {
    position: absolute;
    top: 200px;
    left: 0;
    width: 100%;
    margin: 0;
    font-family: "Alfa Slab One", serif;
    font-weight: 400;
    font-size: 110px;
    line-height: 150px;
    color: var(--cream);
  }
  .brand-name__line { display: block; }
  .rule-set {
    position: absolute;
    left: 0;
    width: 100%;
  }
  .rule-set--upper { top: 585px; }
  .rule-set--lower { top: 905px; }
  .rule-set--base { top: 1062px; }
  .medallion {
    position: absolute;
    left: 210px;
    top: 560px;
    width: 380px;
    height: 330px;
  }
  .medallion__art {
    position: absolute;
    left: 50%;
    top: 50%;
    width: 300px;
    height: 300px;
    margin: -150px 0 0 -150px;
    border-radius: 50%;
    background: radial-gradient(circle, var(--cream) 0%, var(--cream) 46%, var(--tan-dark) 48%, var(--tan) 62%, var(--label-brown) 72%);
  }
  .product-type {
    position: absolute;
    top: 950px;
    left: 0;
    width: 100%;
    margin: 0;
    font-family: "Alfa Slab One", serif;
    font-weight: 400;
    font-size: 96px;
    letter-spacing: 2px;
    color: var(--cream);
    line-height: 1;
  }
  .volume-plate {
    position: absolute;
    top: 1090px;
    left: 300px;
    width: 200px;
    height: 46px;
    background: var(--tan);
    color: var(--label-brown);
    font-family: "Oswald", sans-serif;
    font-weight: 500;
    font-size: 28px;
    line-height: 46px;
    letter-spacing: 2px;
    border-radius: 4px;
  }
</style>
</head>
<body>
  <main class="label">
    <svg class="star-row" width="800" height="60" viewBox="0 0 800 60" aria-hidden="true">
      <g fill="var(--cream)">
        <polygon transform="translate(340 32) scale(0.8)" points="0,-20 5.9,-8 19,-6.2 9.5,3 11.8,16.2 0,10 -11.8,16.2 -9.5,3 -19,-6.2 -5.9,-8"/>
        <polygon transform="translate(400 26) scale(1.1)" points="0,-20 5.9,-8 19,-6.2 9.5,3 11.8,16.2 0,10 -11.8,16.2 -9.5,3 -19,-6.2 -5.9,-8"/>
        <polygon transform="translate(460 32) scale(0.8)" points="0,-20 5.9,-8 19,-6.2 9.5,3 11.8,16.2 0,10 -11.8,16.2 -9.5,3 -19,-6.2 -5.9,-8"/>
      </g>
    </svg>

    <h1 class="brand-name">
      <span class="brand-name__line">Corvel's</span>
      <span class="brand-name__line">Hard</span>
    </h1>

    <svg class="rule-set rule-set--upper" width="800" height="40" viewBox="0 0 800 40" aria-hidden="true">
      <g stroke="var(--blue)" stroke-width="5">
        <line x1="140" y1="10" x2="270" y2="10"/>
        <line x1="160" y1="24" x2="270" y2="24"/>
        <line x1="530" y1="10" x2="660" y2="10"/>
        <line x1="530" y1="24" x2="640" y2="24"/>
      </g>
    </svg>

    <div class="medallion">
      <div class="medallion__art" role="img" aria-label="Illustrated portrait medallion topped with a crown and framed by a laurel wreath"></div>
    </div>

    <svg class="rule-set rule-set--lower" width="800" height="50" viewBox="0 0 800 50" aria-hidden="true">
      <g stroke="var(--blue)" stroke-width="4">
        <line x1="150" y1="18" x2="360" y2="18"/>
        <line x1="440" y1="18" x2="650" y2="18"/>
        <line x1="130" y1="36" x2="670" y2="36"/>
      </g>
      <polygon fill="var(--blue-soft)" transform="translate(400 16) scale(0.9)" points="0,-20 5.9,-8 19,-6.2 9.5,3 11.8,16.2 0,10 -11.8,16.2 -9.5,3 -19,-6.2 -5.9,-8"/>
    </svg>

    <p class="product-type">ROOT BEER</p>

    <svg class="rule-set rule-set--base" width="800" height="12" viewBox="0 0 800 12" aria-hidden="true">
      <line x1="130" y1="6" x2="670" y2="6" stroke="var(--blue)" stroke-width="4"/>
    </svg>

    <div class="volume-plate">355 mL</div>
  </main>
</body>
</html>
```